Property Management business needs Business cards designed

We provide a premium property management service based in Sydney's Norther Beaches. We want people to feel confident in choosing us to manage their investment properties. We offer a much more personalized service than other estate agents.
We want a modern clean design. Something that shows confidence without being complicated.
Logo attached.

Target Market(s)

35-70yo Male and Female with strong property portfolios within Sydney's Norther Beaches

Industry/Entity Type

Property Management

Contact Information for Business Card

Address: Suite 7, 12-14 Kelvin Parade, Harlow NSW 2188
Two separate named cards.
Tom Ardley - 0491 570 118 tom@harbourvaleestates.com.au
Clara Dunmore - 0491 570 263 clara@harbourvaleestates.com.au

Requirements
Must have
• Business logo, name, number, address, email.

```html
<!DOCTYPE html>
<html lang="en">
<head>
<meta charset="utf-8">
<title>Harbourvale Estates – Business Cards</title>
<link rel="stylesheet" href="https://fonts.googleapis.com/css2?family=Arimo:wght@400;700&display=swap">
<style>
  :root {
    --backdrop: #d9d6d0;
    --card: #0c0c0d;
    --card-edge: #1c1c1e;
    --teal: #56c3cf;
    --ink-light: #e9e9e6;
    --rule: #cfcfcf;
  }
  html, body {
    margin: 0;
    padding: 0;
    width: 1200px;
    height: 892px;
    overflow: hidden;
    background: var(--backdrop);
    font-family: "Arimo", Arial, sans-serif;
  }
  .card-sheet {
    position: relative;
    width: 1200px;
    height: 892px;
  }
  .business-card {
    position: absolute;
    left: 250px;
    width: 700px;
    height: 389px;
    background: linear-gradient(160deg, var(--card-edge) 0%, var(--card) 55%);
    border-radius: 6px;
    box-shadow: 0 14px 32px rgba(0,0,0,0.25);
    overflow: hidden;
  }
  .business-card--clara { top: 37px; }
  .business-card--tom { top: 466px; }
  .brand {
    position: absolute;
    left: 36px;
    top: 128px;
    width: 290px;
    display: flex;
    align-items: center;
    gap: 14px;
  }
  .brand-dot {
    flex: none;
    width: 26px;
    height: 26px;
    border-radius: 50%;
    background: var(--teal);
  }
  .brand-name {
    color: var(--ink-light);
    font-weight: 700;
    font-size: 28px;
    line-height: 1.05;
    letter-spacing: 0.5px;
  }
  .divider {
    position: absolute;
    left: 340px;
    top: 60px;
    width: 2px;
    height: 220px;
    background: var(--rule);
  }
  .contact {
    position: absolute;
    right: 36px;
    top: 100px;
    text-align: right;
  }
  .contact-name {
    color: var(--teal);
    font-size: 34px;
    font-weight: 400;
    margin: 0 0 10px;
    line-height: 1.1;
  }
  .contact-row {
    display: flex;
    justify-content: flex-end;
    align-items: center;
    gap: 9px;
    color: var(--ink-light);
    font-size: 17px;
    line-height: 1.6;
  }
  .contact-icon {
    width: 14px;
    height: 14px;
    flex: none;
  }
  .address {
    position: absolute;
    right: 36px;
    bottom: 30px;
    margin: 0;
    color: var(--teal);
    font-size: 26px;
    font-weight: 700;
    letter-spacing: 0.2px;
    white-space: nowrap;
  }
</style>
</head>
<body>
  <main class="card-sheet">
    <article class="business-card business-card--clara">
      <div class="brand">
        <span class="brand-dot"></span>
        <span class="brand-name">HARBOURVALE<br>ESTATES</span>
      </div>
      <div class="divider"></div>
      <section class="contact">
        <h2 class="contact-name">Clara Dunmore</h2>
        <div class="contact-row">
          <span>0491 570 263</span>
          <svg class="contact-icon" viewBox="0 0 16 16" aria-hidden="true">
            <rect width="16" height="16" rx="2" fill="var(--teal)"/>
            <path d="M5 3.5l2 2-1 1.2c.6 1.3 1.5 2.2 2.8 2.8l1.2-1 2 2-1.2 1.5C7.5 12 4 8.5 3.5 4.7z" fill="#0c0c0d"/>
          </svg>
        </div>
        <div class="contact-row">
          <span>clara@harbourvaleestates.com.au</span>
          <svg class="contact-icon" viewBox="0 0 16 16" aria-hidden="true">
            <rect width="16" height="16" rx="2" fill="var(--teal)"/>
            <rect x="3" y="4.5" width="10" height="7" fill="none" stroke="#0c0c0d" stroke-width="1.3"/>
            <path d="M3 4.5l5 4 5-4" fill="none" stroke="#0c0c0d" stroke-width="1.3"/>
          </svg>
        </div>
      </section>
      <p class="address">Suite 7, 12-14 Kelvin Parade, Harlow NSW 2188</p>
    </article>

    <article class="business-card business-card--tom">
      <div class="brand">
        <span class="brand-dot"></span>
        <span class="brand-name">HARBOURVALE<br>ESTATES</span>
      </div>
      <div class="divider"></div>
      <section class="contact">
        <h2 class="contact-name">Tom Ardley</h2>
        <div class="contact-row">
          <span>0491 570 118</span>
          <svg class="contact-icon" viewBox="0 0 16 16" aria-hidden="true">
            <rect width="16" height="16" rx="2" fill="var(--teal)"/>
            <path d="M5 3.5l2 2-1 1.2c.6 1.3 1.5 2.2 2.8 2.8l1.2-1 2 2-1.2 1.5C7.5 12 4 8.5 3.5 4.7z" fill="#0c0c0d"/>
          </svg>
        </div>
        <div class="contact-row">
          <span>tom@harbourvaleestates.com.au</span>
          <svg class="contact-icon" viewBox="0 0 16 16" aria-hidden="true">
            <rect width="16" height="16" rx="2" fill="var(--teal)"/>
            <rect x="3" y="4.5" width="10" height="7" fill="none" stroke="#0c0c0d" stroke-width="1.3"/>
            <path d="M3 4.5l5 4 5-4" fill="none" stroke="#0c0c0d" stroke-width="1.3"/>
          </svg>
        </div>
      </section>
      <p class="address">Suite 7, 12-14 Kelvin Parade, Harlow NSW 2188</p>
    </article>
  </main>
</body>
</html>
```